RJ On Deck: Poster Art Design For A New Musical

We are a non-profit educational theatre company producing a new musical called "RJ On Deck"- a modern retelling of the classic Harold Bexley poem. This upbeat musical comedy features kids in a little league championship tournament and is about teamwork, personal growth and girl power. We are seeking a designer to design a poster for the upcoming production. This poster should include name/logo artwork as well as a full graphic thought for the full image.

Target Market(s)

Teenagers and their parents interested in musical theatre. Edgy but wholesome

Industry/Entity Type

Musical Theatre- sophisticated, Broadway, texture and layers (not kiddie)

Requirements
Must have
• Name of the Show: RJ On Deck
Nice to have
• Baseball themed, A picture of a young girl up at bat, fun colors but photo based, images inside of images, a clean layout, high school appeal

```html
<!DOCTYPE html>
<html lang="en">
<head>
<meta charset="utf-8">
<title>RJ On Deck – Poster</title>
<link rel="stylesheet" href="https://fonts.googleapis.com/css2?family=Oswald:wght@200;700&family=Arimo:wght@400&display=swap">
<style>
  :root {
    --canvas-bg: #c9c9c9;
    --poster-pink: #f2cfd3;
    --poster-rose: #e4a9b3;
    --frame-red: #8a0f16;
    --frame-gray: rgba(120, 110, 115, 0.55);
    --brush-black: #0d0b0b;
    --jersey-red: #b3141c;
    --shorts-navy: #1d1f33;
    --title-gold: #f0b70a;
    --title-rust: #7a1408;
    --title-outline: #9a0c12;
    --streak-red: #d2200e;
    --streak-gold: #ffd24a;
    --info-ink: #1a1a1a;
  }
  * { box-sizing: border-box; margin: 0; padding: 0; }
  html, body {
    width: 1200px; height: 1200px; overflow: hidden;
    background: var(--canvas-bg);
  }
  .poster {
    position: absolute; left: 152px; top: 20px;
    width: 896px; height: 1160px; overflow: hidden;
    background: var(--poster-pink);
  }
  .poster-art { position: absolute; inset: 0; width: 100%; height: 100%; }
  .event-info {
    position: absolute; left: 210px; top: 972px;
    font-family: "Arimo", Arial, sans-serif; font-size: 21px;
    color: var(--info-ink); line-height: 29px;
  }
  .event-info__row { display: flex; align-items: baseline; gap: 6px; }
  .event-info__line {
    display: inline-block; width: 245px;
    border-bottom: 1.5px solid var(--info-ink); transform: translateY(-3px);
  }
</style>
</head>
<body>
  <main class="poster">
    <svg class="poster-art" viewBox="0 0 896 1160" xmlns="http://www.w3.org/2000/svg">
      <defs>
        <linearGradient id="bg-photo-tone" x1="0" y1="0" x2="1" y2="1">
          <stop offset="0" stop-color="#f4d7da"/>
          <stop offset="0.45" stop-color="#e9b7bf"/>
          <stop offset="1" stop-color="#efc9d0"/>
        </linearGradient>
        <linearGradient id="player-tone" x1="0" y1="0" x2="0" y2="1">
          <stop offset="0" stop-color="#b3141c"/>
          <stop offset="0.5" stop-color="#9c1620"/>
          <stop offset="0.7" stop-color="#1d1f33"/>
          <stop offset="1" stop-color="#e8e2e2"/>
        </linearGradient>
        <linearGradient id="streak-tone" x1="0" y1="0" x2="1" y2="0">
          <stop offset="0" stop-color="#d2200e" stop-opacity="0.2"/>
          <stop offset="0.4" stop-color="#ff5a1a"/>
          <stop offset="0.55" stop-color="#ffd24a"/>
          <stop offset="0.8" stop-color="#d2200e"/>
          <stop offset="1" stop-color="#3a0a0a" stop-opacity="0.3"/>
        </linearGradient>
        <linearGradient id="title-fill" x1="0" y1="0" x2="0" y2="1">
          <stop offset="0" stop-color="#6e1208"/>
          <stop offset="0.55" stop-color="#c0620a"/>
          <stop offset="1" stop-color="#f0b70a"/>
        </linearGradient>
      </defs>

      <rect class="background-photo" role="img" aria-label="Large faded photo of a young batter in a striped cap swinging a bat" x="0" y="0" width="896" height="1160" fill="url(#bg-photo-tone)"/>

      <g class="frame frame--gray" fill="none" stroke="var(--frame-gray)" stroke-width="2">
        <rect x="110" y="60" width="670" height="1006"/>
        <rect x="122" y="72" width="646" height="982"/>
      </g>
      <g class="frame frame--red" fill="none" stroke="var(--frame-red)" stroke-width="3">
        <polyline points="155,940 155,121 827,121 827,960"/>
        <polyline points="170,930 170,136 812,136 812,950"/>
      </g>

      <polygon class="brush-stroke" role="img" aria-label="Black paint brush stroke" fill="var(--brush-black)"
        points="6,380 190,318 420,262 620,215 835,168 850,190 780,240 800,270 760,320 780,380 740,420 770,460 730,520 745,600 700,650 560,700 420,715 300,720 160,710 60,690 90,640 40,610 70,560 30,520 60,470 20,430"/>

      <rect class="streak" role="img" aria-label="Glowing red and gold motion streak" x="-60" y="860" width="1020" height="90" fill="url(#streak-tone)" transform="rotate(11 448 905)" opacity="0.9"/>

      <rect class="player-photo" role="img" aria-label="Photo of a young girl in a red cap and jersey swinging a baseball bat" x="190" y="101" width="420" height="860" rx="40" fill="url(#player-tone)"/>

      <g class="show-title" transform="rotate(-17 84 760)">
        <text class="show-title__initials" x="84" y="760" font-family="Oswald, sans-serif" font-weight="200" font-size="300" textLength="175" lengthAdjust="spacingAndGlyphs" fill="url(#title-fill)" stroke="var(--title-outline)" stroke-width="2">RJ</text>
        <text class="show-title__words" x="282" y="760" font-family="Oswald, sans-serif" font-weight="700" font-size="300" textLength="560" lengthAdjust="spacingAndGlyphs" fill="url(#title-fill)" stroke="var(--title-outline)" stroke-width="2">ON DECK</text>
      </g>
    </svg>

    <div class="event-info">
      <div class="event-info__row"><span>DATE:</span><span class="event-info__line"></span></div>
      <div class="event-info__row"><span>TIME:</span><span class="event-info__line"></span></div>
      <div class="event-info__row"><span>PLACE</span><span class="event-info__line"></span></div>
    </div>
  </main>
</body>
</html>
```